Second-Line Parade Announcement

Many members of our local chapter will be heading to New Orleans, LA, USA, in March 2019 to attend a large event hosted by our parent company. As part of this trip, we're hosting our own parade in The French Quarter (famous area of New Orleans), and we want to advertise this particular event, along with 1-2 others, on a one-page flyer.

This should be an invitation. What we're hosting is a "second-line parade," which is a much smaller, personal parade (not like big street parades), usually with 10-20 people.

Target Market(s)

Our own members

Colors

Designer to choose colors to be used in the design.

Requirements
Must have
• - Time & date (4:45 p.m., Sunday, March 17, 2019) and location (French Quarter)
• - Please include imagery of a New-Orleans-style parade (with traditional brass band) *OR* imagery of horn musicians (trumpeter, trombonist, etc.). It does not need to be a photo...could be an illustration...attached some for inspiration
• Final deliverable MUST include designer's raw files (e.g., .AI, .IDML, .PSD, etc.)
Nice to have
• I have included ads from our parent organization for the big conference, which can be used as part of your design or simply as inspiration for your design. I have also enclosed some sketch-like images of musicians that I don't own but that could be used as inspiration.
Should not have
• Please avoid imagery of alcohol, leprechauns (although a tasteful "leprechaun-style" hat would be okay), money/pots of gold and anything 'cartoon-like' or 'child-like.'
• Please leave some room ("white space") for additional details/instructions as they might arise.

```html
<!DOCTYPE html>
<html lang="en">
<head>
<meta charset="utf-8">
<title>Second-Line Parade Flyer</title>
<link rel="stylesheet" href="https://fonts.googleapis.com/css2?family=Cormorant+Garamond:wght@500;600&family=Lobster&family=Oswald:wght@400&family=Montserrat:wght@700&display=swap">
<style>
  :root {
    --green: #17661f;
    --green-dark: #0d3f12;
    --leaf-light: #9ed37a;
    --leaf-mid: #4f9a35;
    --white: #ffffff;
    --ink: #1b1b1b;
    --backdrop: #8a8a8a;
  }
  * { margin: 0; padding: 0; box-sizing: border-box; }
  html, body { width: 1200px; height: 1200px; overflow: hidden; background: var(--backdrop); }
  .flyer {
    position: absolute; left: 191px; top: 12px;
    width: 835px; height: 1165px;
    background: var(--white);
    transform: scale(0.98); transform-origin: top left;
    overflow: hidden;
  }
  .leaf-border {
    position: absolute; left: 0; top: 0; width: 835px; height: 120px;
    background: linear-gradient(180deg, rgba(79,154,53,0.75) 0%, rgba(158,211,122,0.45) 45%, rgba(255,255,255,0) 100%);
  }
  .leaf-side {
    position: absolute; width: 120px; height: 200px;
    background: radial-gradient(ellipse at center, rgba(158,211,122,0.55) 0%, rgba(255,255,255,0) 70%);
  }
  .leaf-side.left { left: -20px; top: 700px; }
  .leaf-side.right { right: -20px; top: 700px; }
  .leaf-side.top-left { left: -30px; top: 60px; height: 240px; }
  .leaf-side.top-right { right: -30px; top: 60px; height: 240px; }

  .brand-mark {
    position: absolute; left: 175px; top: 87px; width: 130px; height: 130px;
    border: 5px solid var(--green); border-radius: 50%;
    display: flex; align-items: center; justify-content: center; text-align: center;
    font-family: "Cormorant Garamond", serif; font-weight: 600; font-size: 17px; line-height: 1.1;
    color: var(--green);
  }
  .brand-divider { position: absolute; left: 330px; top: 110px; width: 2px; height: 89px; background: var(--green); }
  .chapter-name {
    position: absolute; left: 355px; top: 108px;
    font-family: "Cormorant Garamond", serif; font-weight: 500; font-size: 52px; color: var(--green); line-height: 1;
  }
  .chapter-label {
    position: absolute; left: 357px; top: 168px;
    font-family: "Cormorant Garamond", serif; font-weight: 600; font-size: 22px; color: var(--green); letter-spacing: 0.5px;
  }

  .parade-photo {
    position: absolute; left: 23px; top: 262px; width: 789px; height: 448px;
    background:
      radial-gradient(ellipse at 50% 80%, rgba(200,40,30,0.55) 0%, rgba(200,40,30,0) 45%),
      linear-gradient(180deg, #b9c2bd 0%, #5d7a5a 30%, #c9d6e6 60%, #3b3b44 100%);
  }
  .photo-frame { position: absolute; left: 52px; top: 290px; width: 733px; height: 387px; border: 1px solid rgba(255,255,255,0.85); }

  .title-second {
    position: absolute; left: 0; top: 560px; width: 835px; text-align: center;
    font-family: "Lobster", sans-serif; font-size: 118px; color: var(--white); line-height: 1;
    text-shadow: 4px 5px 0 var(--ink);
  }
  .title-parade {
    position: absolute; left: 0; top: 690px; width: 835px; text-align: center;
    font-family: "Lobster", sans-serif; font-size: 124px; color: var(--green); line-height: 1;
    text-shadow: 4px 5px 0 var(--ink);
  }

  .details-ribbon { position: absolute; left: 0; top: 862px; width: 835px; height: 76px; }
  .details-ribbon svg { position: absolute; left: 0; top: 0; }
  .ribbon-text {
    position: absolute; left: 60px; top: 0; width: 715px; height: 76px;
    display: flex; align-items: center; justify-content: space-between;
    font-family: "Oswald", sans-serif; font-size: 32px; color: var(--white);
  }
  .ribbon-text .item { padding: 0 14px; white-space: nowrap; }
  .ribbon-text sup { font-size: 15px; }
  .ribbon-text .sep { width: 2px; height: 56px; background: var(--white); }
  .dot { display: inline-block; width: 9px; height: 9px; border-radius: 50%; background: var(--white); vertical-align: middle; margin: 0 6px; }

  .contact {
    position: absolute; top: 956px;
    font-family: "Montserrat", sans-serif; font-weight: 700; font-size: 17px; color: var(--green); letter-spacing: 0.5px;
  }
  .contact.phone { left: 207px; }
  .contact.web { left: 475px; }

  .notes-box { position: absolute; left: 68px; top: 1005px; width: 707px; height: 133px; border: 2px solid var(--green); }
</style>
</head>
<body>
  <div class="flyer">
    <div class="leaf-border" role="img" aria-label="Shamrock leaf border"></div>
    <div class="leaf-side top-left" role="img" aria-label="Shamrock leaves"></div>
    <div class="leaf-side top-right" role="img" aria-label="Shamrock leaves"></div>
    <div class="leaf-side left" role="img" aria-label="Shamrock leaves"></div>
    <div class="leaf-side right" role="img" aria-label="Shamrock leaves"></div>

    <div class="brand-mark">Northgate<br>Heart<br>Society</div>
    <div class="brand-divider"></div>
    <div class="chapter-name">New York State</div>
    <div class="chapter-label">CHAPTER</div>

    <div class="parade-photo" role="img" aria-label="Photo of a New Orleans brass band marching down a palm-lined street"></div>
    <div class="photo-frame"></div>

    <div class="title-second">Second-Line</div>
    <div class="title-parade">Parade</div>

    <div class="details-ribbon">
      <svg width="835" height="76" viewBox="0 0 835 76">
        <polygon points="28,2 797,2 770,38 797,74 28,74 55,38" fill="var(--green)"/>
      </svg>
      <div class="ribbon-text">
        <span class="item"><span class="dot"></span>17<sup>th</sup> March 2019&nbsp; Sunday</span>
        <span class="sep"></span>
        <span class="item">French Quarter</span>
        <span class="sep"></span>
        <span class="item">4:45 p.m<span class="dot"></span></span>
      </div>
    </div>

    <div class="contact phone">(800) 555-0142</div>
    <div class="contact web">www.northgateheart.org</div>

    <div class="notes-box"></div>
  </div>
</body>
</html>
```